Tidewell Electrical Solutions

On one side. LOGO (underneath:) Commercial Industrial Residential

- NAME & CONTACT DETAILS

Martin K. Oduya
Project Manager

(Cell icon) (441) 555-0187
(Email icon) twlelectricalsoultions@mailpost-demo.com
(Facebook & Instagram icons )@twlelectricalsolutions

Other side: LOGO - underneath ELECTRICAL CONSTRUCTION & MAINTENANCE . LED LIGHTING & AUTOMATION . LIFE SAFETY SYSTEMS (FIRE ALARM / SECURITY) . DATA & COMMUNICATION

```html
<!DOCTYPE html>
<html lang="en">
<head>
<meta charset="utf-8">
<title>Tidewell Electrical Solutions — Business Card</title>
<link href="https://fonts.googleapis.com/css2?family=Montserrat:wght@400;500&family=Roboto+Condensed:wght@700&display=swap" rel="stylesheet">
<style>
  :root {
    --stage: #2b2b2d;
    --teal: #10576b;
    --teal-deep: #0b4354;
    --teal-band: #216476;
    --white: #ffffff;
    --ink: #2c2c2c;
  }
  * { box-sizing: border-box; margin: 0; padding: 0; }
  html, body { width: 1200px; height: 1200px; overflow: hidden; }
  body {
    background: var(--stage);
    font-family: "Montserrat", sans-serif;
    position: relative;
  }
  .card {
    position: absolute;
    left: 285px;
    width: 612px;
    height: 368px;
    overflow: hidden;
  }

  /* Front side */
  .card-front { top: 217px; background: var(--teal); }
  .brand {
    position: absolute;
    top: 0; left: 0; right: 0;
    height: 300px;
    display: flex;
    justify-content: center;
    align-items: center;
    gap: 14px;
  }
  .brand-mark {
    width: 30px; height: 30px;
    background: var(--teal-deep);
  }
  .brand-name {
    font-weight: 500;
    font-size: 24px;
    color: var(--teal-deep);
    white-space: nowrap;
  }
  .services {
    position: absolute;
    left: 71px;
    top: 309px;
    font-size: 11.6px;
    line-height: 17px;
    color: var(--white);
    text-transform: uppercase;
    white-space: nowrap;
  }

  /* Back side */
  .card-back { top: 624px; background: var(--white); }
  .back-brand {
    position: absolute;
    top: 40px; left: 0; right: 0;
    text-align: center;
  }
  .back-brand-name {
    display: inline-flex;
    align-items: center;
    gap: 8px;
    font-weight: 500;
    font-size: 14px;
    color: var(--teal-deep);
  }
  .back-brand-mark {
    width: 12px; height: 12px;
    background: var(--teal-deep);
  }
  .sectors {
    margin-top: 6px;
    font-size: 9.5px;
    color: var(--ink);
    text-transform: uppercase;
    letter-spacing: 1px;
  }
  .identity {
    position: absolute;
    right: 319px;
    top: 156px;
    text-align: right;
  }
  .person-name {
    font-family: "Roboto Condensed", sans-serif;
    font-weight: 700;
    font-size: 22.5px;
    line-height: 26px;
    color: var(--teal-deep);
    text-transform: uppercase;
  }
  .person-role {
    font-size: 11.5px;
    font-weight: 500;
    color: var(--ink);
    margin-top: 1px;
  }
  .divider {
    position: absolute;
    left: 306px;
    top: 153px;
    width: 1px;
    height: 56px;
    background: var(--teal);
  }
  .contacts {
    position: absolute;
    left: 318px;
    top: 153px;
    list-style: none;
    font-size: 11px;
    font-weight: 500;
    color: var(--ink);
    white-space: nowrap;
  }
  .contacts li {
    display: flex;
    align-items: center;
    gap: 5px;
    height: 18.5px;
  }
  .contact-icon { width: 12px; height: 12px; flex: none; }
  .social-dot {
    width: 12px; height: 12px;
    border: 1px solid var(--teal-deep);
    border-radius: 50%;
    flex: none;
  }
  .bottom-band {
    position: absolute;
    left: 0; right: 0; bottom: 0;
    height: 20px;
    background: var(--teal-band);
  }
</style>
</head>
<body>
  <section class="card card-front" aria-label="Card front">
    <div class="brand">
      <div class="brand-mark"></div>
      <div class="brand-name">Tidewell Electrical Solutions</div>
    </div>
    <p class="services">
      Electrical Construction &amp; Maintenance • LED Lighting &amp; Automation<br>
      • Life Safety Systems (Fire Alarm / Security) • Data &amp; Communication
    </p>
  </section>

  <section class="card card-back" aria-label="Card back">
    <div class="back-brand">
      <div class="back-brand-name"><span class="back-brand-mark"></span>Tidewell Electrical Solutions</div>
      <p class="sectors">Commercial · Industrial · Residential</p>
    </div>
    <div class="identity">
      <h1 class="person-name">Martin K. Oduya</h1>
      <p class="person-role">Project Manager</p>
    </div>
    <div class="divider"></div>
    <ul class="contacts">
      <li>
        <svg class="contact-icon" viewBox="0 0 12 12" aria-hidden="true">
          <circle cx="6" cy="6" r="5.4" fill="none" stroke="#0b4354" stroke-width="0.9"/>
          <path d="M4.2 3.4 L5 3.2 L5.5 4.6 L5 5 Q5.4 6.3 6.9 7 L7.3 6.5 L8.6 7.1 L8.4 7.9 Q6.8 8.6 5 6.9 Q3.5 5.2 4.2 3.4 Z" fill="#0b4354"/>
        </svg>
        (441) 555-0187
      </li>
      <li>
        <svg class="contact-icon" viewBox="0 0 12 12" aria-hidden="true">
          <circle cx="6" cy="6" r="5.4" fill="none" stroke="#0b4354" stroke-width="0.9"/>
          <rect x="3.3" y="4.1" width="5.4" height="3.8" fill="none" stroke="#0b4354" stroke-width="0.8"/>
          <path d="M3.3 4.1 L6 6.2 L8.7 4.1" fill="none" stroke="#0b4354" stroke-width="0.8"/>
        </svg>
        twlelectricalsoultions@mailpost-demo.com
      </li>
      <li>
        <span class="social-dot"></span>
        @twlelectricalsolutions
      </li>
    </ul>
    <div class="bottom-band"></div>
  </section>
</body>
</html>
```